Help us share the power of history

We need 5 flyers (they can be similar in design, just small content changes in the front) and 1 large poster.

Paper Lanterns? is a movement that aims to change the history market so that everyone gets what they need to be a changemaker of society. We've been selected as one of the most promising startups in Massachusetts and we will have a booth at FERNFest's Pitch Day.

We are trying to attract the attention of people walking buy to invest in our pledgebarn campaign.

Target Market(s)

500-1,000 social entrepreneurs who are going to be walking around a large convention hall - so everything in terms of colors and design needs to be attractive

Industry/Entity Type

Non Profit

Font styles to use
Other font styles liked:
• Phoenix American

Colors

Designer to choose colors to be used in the design.

Requirements
Must have
• Font type: Phoenix American
• Modern
• Easy to read
• Eye-catching
• Please see attached document for more information.

```html
<!DOCTYPE html>
<html lang="en">
<head>
<meta charset="utf-8">
<title>paper lanterns? — poster</title>
<link rel="stylesheet" href="https://fonts.googleapis.com/css2?family=Economica:wght@400;700&display=swap">
<style>
  :root {
    --orange: #e2431f;
    --vitamin-red: #d93a22;
    --vitamin-red-light: #ea5a3f;
    --ink: #0d0d0d;
    --white: #ffffff;
    --taupe: #6f665a;
    --photo-dark: #3e3e3e;
    --photo-mid: #7a766f;
    --photo-light: #b5b1aa;
  }
  * { margin: 0; padding: 0; box-sizing: border-box; }
  html, body { width: 1200px; height: 2400px; overflow: hidden; background: var(--white); }
  body { font-family: "Economica", "Arial Narrow", sans-serif; color: var(--ink); }
  .poster { position: relative; width: 1200px; height: 2400px; overflow: hidden; background: var(--white); }

  .hero-photo {
    position: absolute; left: 0; top: 0; width: 1200px; height: 1130px;
    background: linear-gradient(180deg, #9c9a96 0%, var(--photo-light) 22%, var(--photo-mid) 40%, #5a5753 62%, var(--photo-dark) 100%);
  }
  .hero-title {
    position: absolute; top: 40px; left: 0; width: 100%; text-align: center;
    font-weight: 700; font-size: 190px; line-height: 1; color: var(--white); letter-spacing: 2px;
  }
  .hero-tagline {
    position: absolute; top: 286px; left: 0; width: 100%; text-align: center;
    font-weight: 700; font-size: 32px; letter-spacing: 5px; color: var(--white);
  }

  .mission-band { position: absolute; left: 0; top: 1040px; width: 1200px; height: 350px; }
  .mission-text {
    position: absolute; top: 1158px; left: 0; width: 100%; text-align: center;
    font-weight: 700; font-size: 50px; line-height: 1.12; color: var(--white);
  }

  .section-title {
    position: absolute; top: 1372px; left: 0; width: 100%; text-align: center;
    font-weight: 700; font-size: 104px; color: var(--ink);
  }
  .service-icon { position: absolute; width: 152px; height: 152px; }
  .service-label {
    position: absolute; font-weight: 700; font-size: 40px; line-height: 1.05;
    text-transform: uppercase; letter-spacing: 1px; color: var(--ink);
  }
  .service-label.left { text-align: right; right: 808px; }
  .service-label.right { left: 784px; }

  .nutrient-band {
    position: absolute; left: 0; top: 1944px; width: 1200px; height: 146px;
    background: var(--taupe); color: var(--white);
    display: flex; align-items: center; justify-content: center; text-align: center;
    font-weight: 700; font-size: 48px; line-height: 1.1;
  }

  .vitamin { position: absolute; top: 2120px; width: 190px; text-align: center; }
  .vitamin-name { font-weight: 700; font-size: 22px; line-height: 1.05; height: 50px; display: flex; align-items: flex-end; justify-content: center; }
  .vitamin-tile {
    width: 84px; height: 84px; margin: 6px auto 8px;
    background: linear-gradient(180deg, var(--vitamin-red-light), var(--vitamin-red));
    color: var(--white); font-weight: 700; font-size: 44px;
    display: flex; align-items: center; justify-content: center;
  }
  .vitamin-note { font-weight: 700; font-size: 22px; line-height: 1.05; }
</style>
</head>
<body>
<main class="poster">
  <div class="hero-photo" role="img" aria-label="Two children wrapped in an American flag standing on a winding desert road lined with wind turbines"></div>
  <h1 class="hero-title">paper lanterns?</h1>
  <p class="hero-tagline">Unleashing the power of history for the future of democracy.</p>

  <svg class="mission-band" viewBox="0 0 1200 350" preserveAspectRatio="none" aria-hidden="true">
    <path d="M0 70 C 300 40, 700 40, 1200 8 L1200 250 C 900 250, 500 270, 0 336 Z" fill="var(--orange)"/>
  </svg>
  <p class="mission-text">We are a systems change initiative to strengthen democracy<br>by enabling everyone to have access to the power of history</p>

  <h2 class="section-title">What we do</h2>

  <p class="service-label left" style="top:1548px;">Frame purpose and<br>power of history</p>
  <svg class="service-icon" style="left:409px; top:1500px;" viewBox="0 0 100 100" aria-hidden="true">
    <circle cx="50" cy="50" r="50" fill="var(--ink)"/>
    <g fill="none" stroke="var(--white)" stroke-width="7" stroke-linecap="round">
      <path d="M28 30 C 45 20, 70 30, 60 50 C 50 70, 30 60, 30 75"/>
      <path d="M72 25 C 72 45, 50 45, 40 50 C 28 58, 50 80, 70 72"/>
    </g>
  </svg>

  <p class="service-label right" style="top:1570px;">Enable innovation</p>
  <svg class="service-icon" style="left:615px; top:1500px;" viewBox="0 0 100 100" aria-hidden="true">
    <circle cx="50" cy="50" r="50" fill="var(--ink)"/>
    <circle cx="50" cy="50" r="27" fill="none" stroke="var(--white)" stroke-width="2" stroke-dasharray="4 4"/>
    <path d="M50 38 a10 10 0 0 1 6 18 v5 h-12 v-5 a10 10 0 0 1 6 -18z" fill="var(--white)"/>
    <rect x="45" y="63" width="10" height="3" fill="var(--white)"/>
    <g fill="var(--white)">
      <circle cx="50" cy="20" r="5"/><circle cx="78" cy="40" r="5"/><circle cx="70" cy="74" r="5"/>
      <circle cx="30" cy="74" r="5"/><circle cx="22" cy="40" r="5"/>
    </g>
  </svg>

  <p class="service-label left" style="top:1780px;">Spread what works</p>
  <svg class="service-icon" style="left:409px; top:1708px;" viewBox="0 0 100 100" aria-hidden="true">
    <circle cx="50" cy="50" r="50" fill="var(--ink)"/>
    <g stroke="var(--white)" stroke-width="6" stroke-linecap="round" fill="var(--white)">
      <line x1="56" y1="44" x2="70" y2="30"/><path d="M62 24 L78 22 L76 38 Z"/>
      <line x1="44" y1="56" x2="30" y2="70"/><path d="M38 76 L22 78 L24 62 Z"/>
      <circle cx="54" cy="46" r="5"/><circle cx="46" cy="54" r="5"/>
    </g>
  </svg>

  <p class="service-label right" style="top:1780px;">Change conversation</p>
  <svg class="service-icon" style="left:615px; top:1708px;" viewBox="0 0 100 100" aria-hidden="true">
    <circle cx="50" cy="50" r="50" fill="var(--ink)"/>
    <path d="M22 24 h36 v22 h-24 l-8 7 v-7 h-4 z" fill="none" stroke="var(--white)" stroke-width="4" stroke-linejoin="round"/>
    <path d="M62 36 h18 v18 h-4 v6 l-7 -6 h-7 z" fill="var(--white)"/>
    <circle cx="34" cy="62" r="6" fill="var(--white)"/>
    <path d="M22 80 a12 10 0 0 1 24 0 z" fill="var(--white)"/>
    <circle cx="66" cy="66" r="6" fill="var(--white)"/>
    <path d="M54 84 a12 10 0 0 1 24 0 z" fill="var(--white)"/>
  </svg>

  <div class="nutrient-band"><p>History, when delivered well, provides people<br>with civic nutrients</p></div>

  <div class="vitamin" style="left:92px;"><p class="vitamin-name">Vitamin<br>Community</p><div class="vitamin-tile">Co</div><p class="vitamin-note">You belong<br>here.</p></div>
  <div class="vitamin" style="left:305px;"><p class="vitamin-name">Vitamin<br>Agency</p><div class="vitamin-tile">Ag</div><p class="vitamin-note">You have<br>power.</p></div>
  <div class="vitamin" style="left:508px;"><p class="vitamin-name">Vitamin<br>Empathy</p><div class="vitamin-tile">Em</div><p class="vitamin-note">You matter.<br>We matter.</p></div>
  <div class="vitamin" style="left:713px;"><p class="vitamin-name">Vitamin<br>Imagination</p><div class="vitamin-tile">Im</div><p class="vitamin-note">You dare to<br>dream.</p></div>
  <div class="vitamin" style="left:886px;"><p class="vitamin-name">Vitamin<br>Context</p><div class="vitamin-tile">Cn</div><p class="vitamin-note">You understand<br>the full picture.</p></div>
</main>
</body>
</html>
```